IT Company based on Biology Business Needs a Business Card Design

We need a business card design for a new company called 'Lumen CELL'. We develop the machine learning solutions especially focused on deep learning algorithms for biology industry. Our initial product is a vision detection on biological images to help doctors diagnose the symptoms. We would like to see designs that use the color green.

Industry/Entity Type

Business

```html
<!DOCTYPE html>
<html lang="en">
<head>
<meta charset="utf-8">
<title>Lumen CELL Business Card</title>
<link href="https://fonts.googleapis.com/css2?family=Open+Sans:wght@400;500;600&display=swap" rel="stylesheet">
<style>
  :root {
    --page-bg: #e9e9e6;
    --card-dark: #1e1e1e;
    --card-light: #ffffff;
    --green-light: #7cc242;
    --green-dark: #138a3e;
    --text-dark: #2e2e2e;
  }
  * { margin: 0; padding: 0; box-sizing: border-box; }
  html, body {
    width: 1200px;
    height: 1000px;
    overflow: hidden;
    background: var(--page-bg);
    font-family: "Open Sans", Arial, sans-serif;
  }
  .card {
    position: absolute;
    left: 265px;
    width: 665px;
    border-radius: 26px;
    box-shadow: 0 6px 18px rgba(0,0,0,0.18);
  }
  .card-front { top: 73px; height: 397px; background: var(--card-dark); }
  .card-back { top: 533px; height: 397px; background: var(--card-light); }

  .brand {
    position: absolute;
    display: flex;
    align-items: center;
    color: var(--green-light);
    font-weight: 500;
    letter-spacing: -1px;
    white-space: nowrap;
  }
  .brand-dot { border-radius: 50%; background: var(--green-light); flex: none; }
  .card-front .brand { left: 140px; top: 158px; font-size: 62px; gap: 22px; }
  .card-front .brand-dot { width: 40px; height: 40px; }
  .card-back .brand { left: 52px; top: 168px; font-size: 44px; gap: 16px; }
  .card-back .brand-dot { width: 30px; height: 30px; }

  .contact { position: absolute; left: 419px; top: 72px; }
  .contact-name { color: var(--green-dark); font-weight: 600; font-size: 21px; letter-spacing: 0.5px; line-height: 1.2; }
  .contact-role { color: var(--green-light); font-size: 17px; line-height: 1.4; }
  .contact-address { margin-top: 36px; color: var(--text-dark); font-size: 16px; line-height: 22px; font-style: normal; }
  .contact-lines { margin-top: 22px; list-style: none; }
  .contact-lines li { display: flex; align-items: center; gap: 8px; color: var(--green-light); font-size: 16px; line-height: 24px; }
  .contact-lines svg { width: 16px; height: 16px; fill: var(--green-dark); flex: none; }
</style>
</head>
<body>
  <section class="card card-front">
    <div class="brand"><span class="brand-dot"></span>LUMEN CELL</div>
  </section>

  <section class="card card-back">
    <div class="brand"><span class="brand-dot"></span>LUMEN CELL</div>
    <div class="contact">
      <p class="contact-name">CLARA REYES</p>
      <p class="contact-role">Manager</p>
      <address class="contact-address">218 Birch Avenue,<br>Suite 40<br>Fairview, OR 97024</address>
      <ul class="contact-lines">
        <li>
          <svg viewBox="0 0 16 16" aria-hidden="true"><path d="M2 5c0-2 2-3 6-3s6 1 6 3v1h-3V5H5v1H2z"/><path d="M4 7h8l2 6H2z"/></svg>
          555 014 2290
        </li>
        <li>
          <svg viewBox="0 0 16 16" aria-hidden="true"><path d="M1 3h14v10H1z"/><path d="M1 3l7 6 7-6" fill="none" stroke="#fff" stroke-width="1.4"/></svg>
          hello@lumencell.com
        </li>
        <li>
          <svg viewBox="0 0 16 16" aria-hidden="true"><circle cx="8" cy="8" r="7"/><path d="M1 8h14M8 1c-3 3-3 11 0 14M8 1c3 3 3 11 0 14" fill="none" stroke="#fff" stroke-width="1.2"/></svg>
          www.lumencell.com
        </li>
      </ul>
    </div>
  </section>
</body>
</html>
```